Velvet Lantern rebranding my business with a new business card

I have my new logo and now I need a refresher on my business cards. I really want something fun and fresh. I like black background or anything to make the color pop.
Logo
Name: Velvet Lantern
Contact Info as stated below:
Mara Pelkin
519-555-0147
Logo
Name: Velvet Lantern
Mara Pelkin
519-555-0147
fb.me/VelvetLanternbyMara
Instagram: @VelvetLanternbyMara

Industry/Entity Type

Business

Contact Information for Business Card

double-sided. Logo on one side. Contact info on the other.

Requirements
Must have
• Logo
• Name: Velvet Lantern
• Contact Info as stated below:
• Mara Pelkin
• 519-555-0147
• fb.me/VelvetLanternbyMara
• fb.me/VelvetLanternbyMara

```html
<!DOCTYPE html>
<html lang="en">
<head>
<meta charset="utf-8">
<title>Velvet Lantern – Business Card</title>
<link rel="stylesheet" href="https://fonts.googleapis.com/css2?family=Crimson+Pro:wght@400;500&family=Lato:wght@400&display=swap">
<style>
  :root {
    --stage: #3b4451;
    --card-white: #fbfbfb;
    --card-shade: #e9e9ea;
    --brand-red: #c1161f;
    --brand-red-deep: #a3121a;
    --ink: #1e1e1e;
    --ring-pink: #f2b9c6;
    --logo-pink: #f0a8c4;
  }
  * { margin: 0; padding: 0; box-sizing: border-box; }
  html, body { width: 1200px; height: 1200px; overflow: hidden; }
  body {
    background: var(--stage);
    position: relative;
    font-family: "Lato", sans-serif;
  }
  .card {
    position: absolute;
    left: 170px;
    width: 860px;
    height: 491px;
    border-radius: 6px;
    overflow: hidden;
    box-shadow: 0 14px 34px rgba(0,0,0,.35);
  }
  .card--front {
    top: 80px;
    background: radial-gradient(ellipse at 35% 30%, var(--card-white) 0%, var(--card-shade) 100%);
  }
  .card--back {
    top: 629px;
    background: radial-gradient(ellipse at 50% 40%, var(--brand-red) 0%, var(--brand-red-deep) 100%);
  }
  .accent-square {
    position: absolute;
    background: var(--brand-red);
  }
  .accent-square--top { left: 0; top: 118px; width: 78px; height: 74px; }
  .accent-square--bottom { left: 392px; bottom: 0; width: 58px; height: 44px; }

  .identity { position: absolute; left: 104px; top: 112px; }
  .identity__company {
    font-family: "Crimson Pro", serif;
    font-weight: 400;
    font-size: 54px;
    line-height: 1;
    color: var(--brand-red);
  }
  .identity__name-row { display: flex; align-items: center; margin-top: 18px; }
  .identity__name {
    font-family: "Crimson Pro", serif;
    font-size: 58px;
    line-height: 1;
    color: var(--ink);
  }
  .identity__rule {
    width: 96px;
    height: 2px;
    background: var(--brand-red);
    margin-left: 16px;
    margin-top: 26px;
  }
  .identity__role {
    font-size: 22px;
    color: var(--brand-red);
    margin-top: 6px;
  }

  .contact {
    position: absolute;
    left: 212px;
    top: 298px;
    list-style: none;
  }
  .contact__item {
    display: flex;
    align-items: center;
    gap: 10px;
    font-size: 21px;
    color: var(--ink);
    line-height: 32px;
  }
  .contact__icon { width: 16px; height: 16px; flex: none; }

  .brand-mark {
    position: absolute;
    display: flex;
    align-items: center;
    justify-content: center;
    text-align: center;
    font-family: "Crimson Pro", serif;
    font-weight: 500;
    color: var(--ink);
  }
  .brand-mark--front {
    right: 70px;
    top: 90px;
    width: 260px;
    height: 260px;
    font-size: 40px;
    line-height: 1.05;
  }
  .brand-seal {
    position: absolute;
    left: 50%;
    top: 50%;
    width: 330px;
    height: 330px;
    margin: -165px 0 0 -165px;
    border-radius: 50%;
    background: var(--card-white);
    box-shadow: inset 0 0 0 10px var(--card-white), inset 0 0 0 13px var(--ring-pink), inset 0 0 0 17px var(--card-white), inset 0 0 0 19px var(--ring-pink);
  }
  .brand-mark--back {
    inset: 0;
    font-size: 44px;
    line-height: 1.05;
  }
</style>
</head>
<body>

<section class="card card--front" aria-label="Business card, contact side">
  <div class="accent-square accent-square--top"></div>
  <div class="accent-square accent-square--bottom"></div>

  <div class="identity">
    <p class="identity__company">Velvet Lantern</p>
    <div class="identity__name-row">
      <p class="identity__name">Mara Pelkin</p>
      <span class="identity__rule"></span>
    </div>
    <p class="identity__role">Director</p>
  </div>

  <ul class="contact">
    <li class="contact__item">
      <svg class="contact__icon" viewBox="0 0 16 16" aria-hidden="true"><path fill="#c1161f" d="M3.6 1.5l2.3 2.8-1.3 1.6c.9 2 2.5 3.6 4.5 4.5l1.6-1.3 2.8 2.3-1.4 2.1C7 13.3 2.7 9 2.5 3z"/></svg>
      519-555-0147
    </li>
    <li class="contact__item">
      <svg class="contact__icon" viewBox="0 0 16 16" aria-hidden="true"><rect x="1" y="3.5" width="14" height="9" rx="1" fill="#c1161f"/><path d="M1.5 4l6.5 5 6.5-5" fill="none" stroke="#fff" stroke-width="1.2"/></svg>
      info@VelvetLantern.com
    </li>
    <li class="contact__item">
      <svg class="contact__icon" viewBox="0 0 16 16" aria-hidden="true"><g fill="none" stroke="#c1161f" stroke-width="1.4"><circle cx="8" cy="8" r="6.5"/><ellipse cx="8" cy="8" rx="3" ry="6.5"/><path d="M1.5 8h13M2.5 4.8h11M2.5 11.2h11"/></g></svg>
      www.VelvetLantern.com
    </li>
    <li class="contact__item">
      <svg class="contact__icon" viewBox="0 0 16 16" aria-hidden="true"><circle cx="8" cy="8" r="7" fill="#c1161f"/></svg>
      fb.me/VelvetLanternbyMara
    </li>
  </ul>

  <div class="brand-mark brand-mark--front">Velvet<br>Lantern</div>
</section>

<section class="card card--back" aria-label="Business card, logo side">
  <div class="brand-seal">
    <div class="brand-mark brand-mark--back">Velvet<br>Lantern</div>
  </div>
</section>

</body>
</html>
```